GravaLoop. Customer needs to know about us, what services we provide & contact us

We are a waste tire recycling company. Our primary focus is on providing a sustainable and cost effective service focusing on: Waste Tire Management, Hassle Free Scheduling for Tire Collection, Mobile Shredding & Special site cleanup services. GravaLoop will be producing TDF, Clean Tire Wire & further materials.
Please look at https://harvonrubber.example
Please look at https://quelbamaterials.example

This is the look and feel of what we want

I have attached a word document with our website info.

Target Market(s)

Tire Install Companies. Such as morbanhaul.example. TDF Purchasers such as pelkofuel.example.

Industry/Entity Type

Waste Tire Recycling

Coding

Coded - Design and coding required

Number of Pages Required

3 page

Font styles to use
Other font styles liked:
• Look at our logo

Requirements
Must have
• We need a 3 page setup for About Us, Services & Contact Us. Contact us should be a form them can fill out and submit to us Images that are related to waste tire recycling. Clean, modern, innovative.
Nice to have
• The color and feel of the website should work with our logo that we did with artpivot
Should not have
• Anything progressive, political or "woke"

```html
<!DOCTYPE html>
<html lang="en">
<head>
<meta charset="utf-8">
<title>GravaLoop — Waste Tire Recycling</title>
<link rel="stylesheet" href="https://fonts.googleapis.com/css2?family=Kanit:ital,wght@0,700;0,800;1,700;1,800&family=Poppins:wght@300;400;500;600&display=swap">
<style>
:root{
  --green:#13923f;
  --green-dark:#0e7a33;
  --ink:#1b1b1b;
  --muted:#666;
  --line:#e3e3e3;
  --footer:#121212;
  --white:#fff;
  --footer-text:#e6e6e6;
}
*{box-sizing:border-box;margin:0;padding:0}
html,body{width:1200px;height:3901px;overflow:hidden}
body{position:relative;font-family:"Poppins",sans-serif;color:var(--ink);background:var(--white)}
.abs{position:absolute}
.display{font-family:"Kanit",sans-serif;font-weight:800;font-style:italic}
.ph{position:absolute}
.brand{font-family:"Poppins",sans-serif;font-weight:600;color:var(--green);display:flex;align-items:center;gap:10px}
.brand .dot{width:22px;height:22px;border-radius:50%;background:var(--green)}

/* header */
.header-white{left:0;top:0;width:397px;height:83px;background:var(--white)}
.header-logo{left:60px;top:24px;font-size:28px}
.nav{right:290px;top:32px;display:flex;gap:24px;font-size:12px;color:var(--ink)}
.nav a{color:inherit;text-decoration:none}
.nav .active{color:var(--green);border-bottom:2px solid var(--green);padding-bottom:6px}
.call-btn{left:979px;top:18px;width:161px;height:42px;background:var(--green);border-radius:8px;color:#fff;display:flex;align-items:center;justify-content:center;gap:10px;font-size:16px;font-weight:500}

/* hero */
.hero-left{left:0;top:83px;width:397px;height:555px;background:linear-gradient(160deg,#5b5b55,#2a2c29 60%,#4a4f3c)}
.hero-right{left:397px;top:0;width:803px;height:642px;background:linear-gradient(180deg,#8e959c 0%,#a7acb0 35%,#4d524f 60%,#6b6d69 100%)}
.hero-card{left:197px;top:259px;width:341px;height:453px;background:var(--green);border-radius:12px;color:#fff;text-align:center;padding-top:110px}
.hero-card h1{font-size:58px;line-height:1;letter-spacing:1px}
.hero-card .sub{font-size:52px;line-height:1.05;color:transparent;-webkit-text-stroke:1.5px #fff;opacity:.9}
.hero-card p{font-size:13px;font-style:italic;line-height:1.75;margin:28px 24px 0}
.outline-btn{display:inline-block;margin-top:24px;border:1.5px solid #fff;border-radius:10px;padding:10px 18px;font-size:15px;font-weight:500;color:#fff}

/* welcome */
.section-title{width:1200px;left:0;text-align:center;font-size:38px;line-height:1.2}
.section-title .g{color:var(--green)}
.center-sub{width:1200px;left:0;text-align:center;font-size:16px;color:#333}
.welcome-lead{left:330px;top:872px;width:540px;text-align:center;font-size:13.5px;line-height:1.6;color:var(--green)}
.photo-worker{left:117px;top:956px;width:483px;height:376px;background:linear-gradient(135deg,#3d434a,#787f86 50%,#c9742e 75%,#8a8f92)}
.photo-crumb{left:600px;top:1332px;width:484px;height:389px;background:linear-gradient(180deg,#7fa8d6 0%,#c9d7e4 35%,#6b6e70 55%,#222 100%)}
.copy{font-size:11.5px;line-height:1.7;color:#555}
.copy p+p{margin-top:14px}
.stand{left:117px;top:1648px;font-size:18px;color:var(--green);line-height:1.3}
.stand u{text-underline-offset:3px}

/* services */
.svc-band{left:0;top:1801px;width:338px;height:494px;background:var(--green)}
.svc-title{left:145px;top:1862px;font-size:36px;color:#fff}
.svc-title .b{color:var(--ink)}
.svc-sub{left:148px;top:1912px;font-size:16px;color:#fff}
.svc-card{top:1974px;width:211px;height:235px;background:#fff;border:1px solid var(--line);text-align:center;padding-top:26px}
.svc-card .icon{width:72px;height:72px;margin:0 auto}
.svc-card h3{font-size:13.5px;font-weight:500;line-height:1.55;margin-top:16px;height:44px;display:flex;align-items:center;justify-content:center}
.svc-card a{display:inline-block;margin-top:14px;font-family:"Kanit",sans-serif;font-weight:700;font-style:italic;font-size:15px;color:var(--green)}

/* stats */
.stat-icon{left:147px;top:2397px;width:100px;height:96px;background:var(--green);border-radius:14px}
.stat-num{left:280px;top:2378px;font-size:66px;color:#9aa69a;line-height:1}
.stat-label{left:281px;top:2456px;font-size:17px}
.divider{left:601px;top:2372px;width:1px;height:128px;background:var(--line)}
.quote{left:660px;top:2382px;width:380px;text-align:center;font-size:14px;line-height:1.65;color:#555}
.qmark{font-family:"Kanit",sans-serif;font-weight:800;color:var(--green);font-size:34px;line-height:1}
.client{left:660px;top:2487px;width:380px;text-align:center;font-size:14px;font-weight:600;color:var(--green)}

/* products */
.prod-block{left:712px;top:2604px;width:488px;height:449px;background:var(--green)}
.prod-photo{left:641px;top:2656px;width:498px;height:374px;background:linear-gradient(135deg,#e0b622,#3b4654 35%,#5a6672 60%,#1f1f1f)}
.prod-title{left:126px;top:2664px;font-size:34px;line-height:1.2}
.prod-title .g{color:var(--green)}
.prod-copy{left:126px;top:2763px;width:425px}
.solid-btn{background:var(--green);color:#fff;border-radius:8px;font-size:16px;font-weight:500;display:flex;align-items:center;justify-content:center}

/* contact */
.basket{left:164px;top:3280px;width:280px;height:227px;background:linear-gradient(180deg,#2a2a2a 0%,#3b3b3b 38%,#2fa24f 40%,#1e8a3c 100%);border-radius:10px}
.attach{left:232px;top:3525px;font-size:17px;color:var(--green);display:flex;gap:8px;align-items:center}
.field{height:40px;border:1px solid var(--line);border-radius:10px;font-size:11.5px;color:#555;padding:12px 16px}
.field.msg{height:88px}

/* footer */
.footer{left:0;top:3663px;width:1200px;height:238px;background:var(--footer)}
.foot-logo{left:60px;top:3728px;font-size:34px}
.copyright{left:60px;top:3800px;font-size:12px;color:var(--footer-text)}
.copyright span{color:var(--green)}
.foot-h{font-size:15px;font-weight:600;color:var(--green)}
.foot-h b{color:#fff;font-weight:600}
.sitemap{left:735px;top:3711px;color:var(--footer-text)}
.sitemap ul{list-style:none;margin-top:22px;font-size:11.5px;line-height:26px}
.sitemap li::before{content:"";display:inline-block;width:5px;height:5px;border-radius:50%;background:var(--green);margin:0 14px 2px 0}
.foot-contact{left:947px;top:3711px;color:var(--footer-text)}
.foot-contact .row{display:flex;align-items:center;gap:16px;font-size:12px;margin-top:14px}
.social{display:flex;gap:8px;margin-top:22px}
.social span{width:33px;height:33px;background:var(--green);border-radius:6px}
</style>
</head>
<body>

<!-- header -->
<div class="abs hero-right ph" role="img" aria-label="Tire recycling plant with piles of scrap tires under a cloudy sky"></div>
<div class="abs hero-left ph" role="img" aria-label="Heap of discarded tires in a field"></div>
<div class="abs header-white"></div>
<div class="abs header-logo brand"><span class="dot"></span>GravaLoop</div>
<nav class="abs nav">
  <a class="active" href="#">HOME</a><a href="#">ABOUT US</a><a href="#">SERVICES</a><a href="#">CONTACT US</a>
</nav>
<div class="abs call-btn">
  <svg width="18" height="18" viewBox="0 0 24 24" fill="#fff"><path d="M6.6 10.8a15.1 15.1 0 0 0 6.6 6.6l2.2-2.2a1 1 0 0 1 1-.25 11.4 11.4 0 0 0 3.6.57 1 1 0 0 1 1 1V20a1 1 0 0 1-1 1A17 17 0 0 1 3 4a1 1 0 0 1 1-1h3.5a1 1 0 0 1 1 1c0 1.25.2 2.45.57 3.57a1 1 0 0 1-.25 1z"/></svg>
  555 010 4821
</div>

<div class="abs hero-card">
  <h1 class="display">WasteTire</h1>
  <div class="sub display">Recycling</div>
  <p>You've Got A Business To Run, And We've Got You Covered. Let Us Worry About Your Scrap Tire Removal So You Don't Have To.</p>
  <span class="outline-btn">CONTACT US</span>
</div>

<!-- welcome -->
<h2 class="abs section-title display" style="top:776px"><span class="g">Welcome To</span> GravaLoop</h2>
<div class="abs center-sub" style="top:832px">Waste Tire Recycling</div>
<p class="abs welcome-lead">GravaLoop is forging the wat towards a more sustainable future through scrap tire collection &amp; waste tire recycling</p>

<div class="abs photo-worker ph" role="img" aria-label="Worker in orange overalls stacking used tires"></div>
<div class="abs copy" style="left:654px;top:1002px;width:356px">
  <p>You've got a business to run, and we've got you covered. Let us worry about your scrap tire removal so you don't have to. Through the use of innovative technologies, we are not only more eco-friendly but able to pass the savings along to our customers.</p>
  <p>Waste Tire Management is a global problem that GravaLoop aims to resolve. Though our innovative approach to waste tire management, we are focused on resolving environmental concerns head-on. All while giving businesses across the region an opportunity to make a difference for the environment and their bottom line.</p>
</div>

<div class="abs photo-crumb ph" role="img" aria-label="Conveyor dropping shredded rubber onto a pile outside a warehouse"></div>
<div class="abs copy" style="left:117px;top:1397px;width:405px">
  <p>Built upon a foundation of innovation, attention to detail, &amp; budget-conscious services, GravaLoop is at the forefront of pushing the boundaries of what can be achieved through advancing technology. Through our rigorous procedures, environmental commitment we go beyond expectations. GravaLoop aims to achieve efficiency all while revolutionizing the industry.</p>
  <p>When your company is deciding on used-tire disposal responsib-ilities you can rest assured that GravaLoop has your company's interest at its core. Leave the costly equipment, manpower, &amp; output-reducing duties to us. GravaLoop will help you focus your time where it counts.</p>
</div>
<div class="abs stand display">Here At GravaLoop We're Making A Stand.<br>Are You <u>Joining Us</u></div>

<!-- services -->
<div class="abs svc-band"></div>
<h2 class="abs svc-title display">Our <span class="b">Services</span></h2>
<div class="abs svc-sub">Waste Tire Recycling</div>

<div class="abs svc-card" style="left:147px">
  <svg class="icon" viewBox="0 0 72 72" fill="none" stroke="#111" stroke-width="3"><circle cx="36" cy="36" r="30"/><circle cx="36" cy="36" r="16"/><circle cx="50" cy="48" r="10" fill="#13923f" stroke="#111"/></svg>
  <h3>WASTE TIRE MANAGEMENT<br>&amp; RECYCLING</h3><a>Learn More</a>
</div>
<div class="abs svc-card" style="left:379px">
  <svg class="icon" viewBox="0 0 72 72" fill="none" stroke="#111" stroke-width="3"><circle cx="36" cy="34" r="28"/><circle cx="36" cy="34" r="14" fill="#13923f"/><path d="M40 52v14h16V50"/></svg>
  <h3>TIRE REMEDIATION &amp;<br>SPECIAL TIRE CLEAN-UPS</h3><a>Learn More</a>
</div>
<div class="abs svc-card" style="left:611px">
  <svg class="icon" viewBox="0 0 72 72" fill="none" stroke="#111" stroke-width="3"><rect x="6" y="10" width="60" height="54" rx="4"/><path d="M6 22h60"/><g fill="#13923f" stroke="none"><rect x="13" y="29" width="10" height="8"/><rect x="31" y="29" width="10" height="8"/><rect x="49" y="29" width="10" height="8"/><rect x="13" y="43" width="10" height="8"/><rect x="31" y="43" width="10" height="8"/><rect x="49" y="43" width="10" height="8"/></g></svg>
  <h3>SCHEDULING &amp;<br>BILLING</h3><a>Learn More</a>
</div>
<div class="abs svc-card" style="left:842px">
  <svg class="icon" viewBox="0 0 72 72" fill="none" stroke="#111" stroke-width="3"><circle cx="36" cy="24" r="12"/><path d="M22 24a14 14 0 0 1 28 0" stroke="#13923f" stroke-width="5"/><path d="M10 66c0-14 12-22 26-22s26 8 26 22z"/></svg>
  <h3>FIRST RATE CUSTOMER<br>SUPPORT &amp; SERVICE</h3><a>Learn More</a>
</div>

<!-- stats -->
<div class="abs stat-icon ph" role="img" aria-label="Recycling emblem"></div>
<div class="abs stat-num display">1,10,96</div>
<div class="abs stat-label">Tires Recycled by GravaLoop</div>
<div class="abs divider"></div>
<span class="abs qmark" style="left:656px;top:2370px">“</span>
<p class="abs quote">Lorem Ipsum has been the industry's standard dummy text e er since the when an unknown printer took a galley of to make a type specimen book. It has survi ed not only fi e centuries</p>
<span class="abs qmark" style="left:978px;top:2450px">”</span>
<div class="abs client">— &nbsp;Client Name</div>

<!-- products -->
<div class="abs prod-block"></div>
<div class="abs prod-photo ph" role="img" aria-label="Yellow conveyor belt carrying tire-derived fuel chips"></div>
<h2 class="abs prod-title display"><span class="g">Products</span><br>TDS</h2>
<div class="abs copy prod-copy">
  <p>GravaLoop seeks to be one of the leading TDF suppliers to the region. This is a product with a wide range of demand from pulp and paper mills, electrical utilities, industrial boilers to cement and asphalt plants our expertly handled tire-derived fuel is being used and receiving high marks for its ever-expanding list of benefits.</p>
  <p>From driving boiler efficiency to stamping out emissions, GravaLoop wants to be your TDF supplier offering additional services to include tire pick-up to TDF drop-off we have your back!</p>
</div>
<div class="abs solid-btn" style="left:124px;top:2948px;width:139px;height:40px">CONTACT US</div>

<!-- contact -->
<h2 class="abs section-title display" style="top:3136px"><span class="g">Get In</span> Touch</h2>
<p class="abs center-sub" style="top:3194px;left:360px;width:480px;font-size:13.5px;line-height:1.55">If You Have Any Questions, Just Fill In The Contact Form, And We Will Be In Contact Shortly</p>

<div class="abs basket ph" role="img" aria-label="Green recycling bin filled with used tires"></div>
<div class="abs attach">
  <svg width="20" height="20" viewBox="0 0 24 24" fill="none" stroke="#13923f" stroke-width="2"><path d="M21 11l-8.5 8.5a5 5 0 0 1-7-7L14 4a3.5 3.5 0 0 1 5 5l-8.5 8.5a2 2 0 0 1-3-3L15 7"/></svg>
  Attach Image
</div>

<div class="abs field" style="left:535px;top:3280px;width:259px">Company Name *</div>
<div class="abs field" style="left:805px;top:3280px;width:259px">Address of Business for PickUp *</div>
<div class="abs field" style="left:535px;top:3336px;width:259px">Email *</div>
<div class="abs field" style="left:805px;top:3336px;width:259px">Number of tires *</div>
<div class="abs field" style="left:535px;top:3391px;width:259px">Phone *</div>
<div class="abs field" style="left:805px;top:3391px;width:259px">Pickup Frequency *</div>
<div class="abs field msg" style="left:535px;top:3444px;width:529px">Message *</div>
<div class="abs solid-btn" style="left:535px;top:3547px;width:109px;height:41px">SUBMIT</div>

<!-- footer -->
<footer class="abs footer"></footer>
<div class="abs foot-logo brand"><span class="dot"></span>GravaLoop</div>
<div class="abs copyright">©<span>GravaLoop</span> - 2022 All rights reserved.</div>
<div class="abs sitemap">
  <div class="foot-h">SITE<b>MAP</b></div>
  <ul><li>Home</li><li>About Us</li><li>Services</li><li>Contact Us</li></ul>
</div>
<div class="abs foot-contact">
  <div class="foot-h">CONTACT <b>US</b></div>
  <div class="row" style="margin-top:20px">
    <svg width="18" height="18" viewBox="0 0 24 24" fill="#13923f"><path d="M6.6 10.8a15.1 15.1 0 0 0 6.6 6.6l2.2-2.2a1 1 0 0 1 1-.25 11.4 11.4 0 0 0 3.6.57 1 1 0 0 1 1 1V20a1 1 0 0 1-1 1A17 17 0 0 1 3 4a1 1 0 0 1 1-1h3.5a1 1 0 0 1 1 1c0 1.25.2 2.45.57 3.57a1 1 0 0 1-.25 1z"/></svg>
    555 010 4821
  </div>
  <div class="row">
    <svg width="18" height="14" viewBox="0 0 24 18" fill="#13923f"><rect width="24" height="18" rx="2"/><path d="M2 3l10 7 10-7" stroke="#121212" stroke-width="2" fill="none"/></svg>
    info@gravaloop.example
  </div>
  <div class="social"><span></span><span></span><span></span></div>
</div>

</body>
</html>
```